Web design for business website

I need a web design for a business website for one of our clients who is specialized in alarm management software. I would like you to design 3 web pages, one for each of the 3 pages. You need to process the corporate identity of our client to the web design. This means the colors of the logo (red and black) should definitely show up on all of the 3 pages. Find the logo file for the logo of our customer. To increase readability I suggest you use a white/light background. All suggestions are welcome.

Please kindly download atttached Webdesign.zip and read the project brief first. The project brief refers to all other files of the zip file. Your design must have exactly the same structure as the wireframes.
Updates

Target Market(s)

B2B, Alarm management

Industry/Entity Type

Business

Number of Pages Required

3 page

Requirements
Must have
• The web design must have exactly the same structure as the wireframes and needs to contain the colors of the company logo.

```html
<!DOCTYPE html>
<html lang="en">
<head>
<meta charset="utf-8">
<title>LOGIRA – Real-time reasoning solutions</title>
<link href="https://fonts.googleapis.com/css2?family=Lato:wght@300;400;700;900&display=swap" rel="stylesheet">
<style>
:root{
  --accent:#ee4a1c;
  --navy:#1d1a33;
  --ink:#2b2a35;
  --text:#555;
  --muted:#777;
  --line:#ddd;
  --paper:#fff;
  --soft:#f5f4f5;
  --footer:#ebebec;
}
*{box-sizing:border-box;margin:0;padding:0}
html,body{width:1200px;height:1120px;overflow:hidden}
body{font-family:'Lato',sans-serif;color:var(--ink);background:var(--paper);font-size:12px}
.wrap{width:650px;margin:0 auto;position:relative;height:100%}
a{color:inherit;text-decoration:none}

.topbar{height:27px;border-bottom:1px solid var(--line)}
.topbar .wrap{display:flex;align-items:center;justify-content:space-between}
.phone{font-size:10px;color:var(--ink);margin-left:2px}
.top-tools{display:flex;gap:6px}
.lang{width:54px;height:21px;border:1px solid #ccc;display:flex;align-items:center;font-size:9px;font-weight:700;padding-left:5px;position:relative}
.lang::after{content:"";position:absolute;right:0;top:0;width:18px;height:100%;border-left:1px solid #ccc}
.lang svg{position:absolute;right:5px;top:8px}
.search{width:126px;height:21px;border:1px solid #ccc;font-size:9px;color:#999;padding:5px 6px}

.header{height:67px;border-bottom:1px solid var(--line)}
.header .wrap{display:flex;align-items:center;justify-content:space-between}
.brand{display:flex;align-items:center;gap:8px}
.brand-mark{width:34px;height:34px;border-radius:50%;background:var(--accent)}
.brand-name{font-size:26px;font-weight:900;letter-spacing:1.5px;color:var(--ink);line-height:1}
.brand-tag{font-size:8px;color:var(--ink);margin-top:2px}
.auth{display:flex;gap:4px}
.btn{height:26px;width:74px;display:flex;align-items:center;justify-content:center;font-size:9px;background:#f0f0f0;border:1px solid #ccc;color:#555}
.btn.primary{background:var(--accent);border-color:var(--accent);color:#fff;width:74px}

.nav{height:28px}
.nav ul{list-style:none;display:flex;gap:0;height:100%;align-items:center}
.nav li{font-size:10px;color:#555;margin-right:40px}
.nav li.active{color:var(--accent)}

.hero{height:317px;position:relative;background:linear-gradient(180deg,#3a3650 0%,#2a2740 55%,#1c1a2e 100%)}
.hero-text{position:absolute;top:213px;width:100%;text-align:center;color:#fff;font-size:15px}
.hero-text em{font-style:normal;color:var(--accent)}
.dots{position:absolute;top:279px;width:100%;display:flex;justify-content:center;gap:4px}
.dots span{width:8px;height:8px;border-radius:50%;background:#fff}
.dots span.on{background:var(--accent)}

.section-title{text-align:center;font-size:21px;font-weight:300}
.section-title b{font-weight:700}
.rule{width:107px;margin:6px auto 0;border-top:1px solid #999;border-bottom:1px solid #999;height:3px}

.welcome{height:226px;background:var(--soft);padding-top:40px}
.welcome .section-title{color:var(--ink)}
.welcome p{width:548px;margin:17px auto 0;text-align:center;font-size:8.3px;line-height:15px;color:var(--text)}

.clients{height:175px;background:var(--navy);padding-top:33px}
.clients .section-title{color:#fff}
.clients .rule{border-color:#aaa}
.client-strip{margin:17px auto 0;width:650px;height:58px;background:#fff;display:flex;align-items:center;justify-content:space-around;padding:0 8px}
.client{font-size:14px;font-weight:700;color:#888;display:flex;align-items:center;gap:5px}
.client i{width:14px;height:14px;border-radius:50%;background:#aaa;display:block}

.social{height:34px;background:#fff}
.social .wrap{display:flex;align-items:center;justify-content:space-between}
.social-links{display:flex;gap:24px;font-size:13px;font-weight:900}
.social-links .s1{color:var(--navy)}
.social-links .s2,.social-links .s3{color:var(--accent)}
.subscribe{display:flex}
.subscribe span{width:186px;height:22px;border:1px solid var(--accent);font-size:8.5px;color:var(--accent);padding:5px 6px}
.subscribe b{width:81px;height:22px;background:var(--accent);color:#fff;font-size:9px;display:flex;align-items:center;justify-content:center;font-weight:700}

.footer{height:209px;background:var(--footer)}
.footer .wrap{display:flex}
.cols{display:flex;padding-top:19px;width:472px}
.col{width:120px}
.col h4{font-size:11px;font-weight:400;color:var(--ink);width:104px;padding-bottom:6px;border-bottom:3px double #bbb}
.col ul{list-style:none;margin-top:10px}
.col li{font-size:8.5px;color:#444;line-height:17.5px}
.col li.active{color:var(--accent);text-decoration:underline}
.contact{position:absolute;right:7px;top:0;width:177px;height:209px;background:var(--navy);color:#fff;padding:18px 0 0 24px}
.contact .brand-mark{width:25px;height:25px;background:#ccc}
.contact .brand-name{font-size:19px;color:#ddd}
.contact .brand-tag{color:#bbb;font-size:6.5px}
.contact p{font-size:8.5px;line-height:14px;margin-top:12px}
.contact .row{display:flex;align-items:center;gap:8px;font-size:8.5px;margin-top:10px}
.contact .row svg{flex:none}

.copyright{height:32px;display:flex;align-items:center;justify-content:center;font-size:8px;color:#888;border-bottom:1px solid var(--line)}
</style>
</head>
<body>
<div class="topbar"><div class="wrap">
  <span class="phone">T +00 (0) 12 3456 789</span>
  <div class="top-tools">
    <div class="lang">ENG<svg width="7" height="4"><path d="M0 0h7L3.5 4z" fill="#777"/></svg></div>
    <div class="search">Search</div>
  </div>
</div></div>

<header class="header"><div class="wrap">
  <div class="brand">
    <div class="brand-mark"></div>
    <div><div class="brand-name">LOGIRA</div><div class="brand-tag">Real-time reasoning solutions</div></div>
  </div>
  <div class="auth">
    <a class="btn">ACCOUNT</a><a class="btn">LOGIN</a><a class="btn primary">SIGN UP</a>
  </div>
</div></header>

<nav class="nav"><div class="wrap"><ul>
  <li class="active">Home</li><li>Industry</li><li>Telecom</li><li>Power</li><li>Utilities</li><li>Infra</li><li>Store</li>
</ul></div></nav>

<section class="hero" role="img" aria-label="Photo looking up between tall glass office towers into a cloudy sky, dark blue tint">
  <div class="hero-text">A perfect Blend of <em>CREATIVITY</em> with <em>SIMPLICITY</em> enhancing your business</div>
  <div class="dots"><span class="on"></span><span></span><span></span></div>
</section>

<section class="welcome">
  <h2 class="section-title">Welcome to <b>LOGIRA</b></h2>
  <div class="rule"></div>
  <p>Companies have invested to get data out of processes. New technologies have been developed to get real-time data out of the harshest places, like oil-well drill heads or the Great Barrier Riff. Data in itself means nothing without the context the data is collected in. Example: data from equipment under maintenance does not provide information to operations. Information - data which is valid and meaningful - can overwhelm any user without the proper knowledge to interpret this information. LOGIRA technology enables easy application of such knowledge in a comprehensible – visual – representation and makes hypothetical reasoning with information possible providing meaningful advisories to subscribers when they need it or when it is required that they are made aware of a situation which requires their attention.</p>
</section>

<section class="clients">
  <h2 class="section-title">Our <b>CLIENTS</b></h2>
  <div class="rule"></div>
  <div class="client-strip">
    <span class="client"><i></i>Norvane</span>
    <span class="client">Keltrix</span>
    <span class="client">Brauwell</span>
    <span class="client">petromond</span>
    <span class="client"><i></i>HALVERN</span>
    <span class="client">Qasira</span>
    <span class="client">Corrix</span>
  </div>
</section>

<div class="social"><div class="wrap">
  <div class="social-links"><span class="s1">Chirpline</span><span class="s2">ViewTube</span><span class="s3">WorkNet</span></div>
  <div class="subscribe"><span>Enter Your Email Address</span><b>SUBSCRIBE</b></div>
</div></div>

<footer class="footer"><div class="wrap">
  <div class="cols">
    <div class="col"><h4>Solutions</h4><ul><li>AMX Alarm Reporting</li><li class="active">AMX Alarm Analysis</li><li>AMX Alarm Expert</li><li>USE</li></ul></div>
    <div class="col"><h4>Industries</h4><ul><li>Industry</li><li>Telcom</li><li>Power</li><li>Utilities</li><li>Infra</li></ul></div>
    <div class="col"><h4>About Us</h4><ul><li>Company</li><li>Overview</li><li>Leadership</li><li>Partners</li><li>Location</li></ul></div>
    <div class="col"><h4>News</h4><ul><li>Product News</li><li>Partner News</li><li>Events</li><li>Press Releases</li><li>Vacancies</li></ul></div>
  </div>
  <div class="contact">
    <div class="brand">
      <div class="brand-mark"></div>
      <div><div class="brand-name">LOGIRA</div><div class="brand-tag">Real-time reasoning solutions</div></div>
    </div>
    <p>#123, Street Name, City Name<br>Country CH - 1234</p>
    <div class="row"><svg width="18" height="18" viewBox="0 0 18 18"><circle cx="9" cy="9" r="8" fill="none" stroke="#fff"/><path d="M6 5l2 0 1 2.5-1.2 1a5 5 0 0 0 2.7 2.7l1-1.2 2.5 1v2c-4 .3-8-3.7-8-8z" fill="#fff"/></svg>(44) 234 234 2345</div>
    <div class="row"><svg width="18" height="18" viewBox="0 0 18 18"><circle cx="9" cy="9" r="8" fill="none" stroke="#fff"/><rect x="5" y="6" width="8" height="6" fill="#fff"/><path d="M5 6l4 3.5L13 6" fill="none" stroke="#1d1a33" stroke-width=".8"/></svg>info@example.com</div>
    <p style="margin-top:20px">#123, Street Name, City Name<br>Country CH - 1234</p>
  </div>
</div></footer>

<div class="copyright">Copyright 2015 LOGIRA. All Rights Reserved.</div>
</body>
</html>
```